New IPv6 service needs a Web Design

We're launching a brand new service which is designed to connect the current Internet Protocol (IPv4) to the new Internet Protocol (IPv6).
The logo can be found at http://www.lumaport.example
We're looking for a clean and simple design, nothing super-fancy. There has to be room for some menu items and a place where people can login (so an e-mail and password box and login button, which must be replaced by the username and a logout button when the user is logged in).
We need a place for a rotating billboard (see http://vq.example for an example) or a video.
Designs that incorporate IPv4 - IPv6 elements (images with interconnecting networks, videos doing the same) will be rated higher, although the basic design is still the primary concern.
We need :
- A main page, with the rotating billboard and some other typical main page stuff
- 2 subpages with different formatted content blocks (1 column and 2 column)
This is a very short design contest, since we intend to go live very soon. Decision will be made quickly.
PSD file is sufficient, but it must be easy to slice to HTML/CSS (but we'll do that part ourselves).
Target Market(s)
IT Professionals
Industry/Entity Type
Internet
Look and feel
Each slider illustrates characteristics of the customer's brand and the style your logo design should communicate.

```html
<!DOCTYPE html>
<html lang="en">
<head>
<meta charset="utf-8">
<title>Lumaport – IPv6 Service</title>
<link href="https://fonts.googleapis.com/css2?family=Roboto:wght@400;500;700&display=swap" rel="stylesheet">
<style>
  :root{
    --navy:#1d5a86;
    --blue:#3f7fb6;
    --red:#d8262c;
    --ink:#333;
    --muted:#777;
    --page:#f4f4f4;
    --footer:#e6e6e6;
    --btn-dark:#4a4a4a;
    --scrim:rgba(70,70,72,.55);
  }
  *{box-sizing:border-box;margin:0;padding:0}
  html,body{width:1200px;height:1181px;overflow:hidden}
  body{font-family:"Roboto",Arial,sans-serif;background:var(--page);color:var(--ink);position:relative}
  .abs{position:absolute}
  .top-bar{left:0;top:0;width:1200px;height:6px;background:var(--navy)}
  .login-tab{left:920px;top:6px;width:83px;height:21px;background:var(--blue);border-radius:0 0 5px 5px;color:#fff;font-size:11px;display:flex;align-items:center;justify-content:center;gap:5px}
  .login-tab i{width:8px;height:8px;background:#fff;border-radius:1px;display:inline-block}
  .brand{font-weight:700;color:var(--navy);letter-spacing:-1px}
  .site-logo{left:213px;top:50px;font-size:50px}
  .main-nav{left:556px;top:81px;display:flex;gap:30px;font-size:12.5px;color:var(--blue)}
  .main-nav span:first-child{color:var(--ink)}
  .hero-title{left:213px;top:176px;font-size:26.5px;line-height:27px;width:300px;color:var(--ink)}
  .hero-title .r{color:var(--red)}.hero-title .b{color:var(--blue)}
  .read-more{display:flex;align-items:center;gap:12px;background:linear-gradient(#5a5a5a,#3a3a3a);color:#fff;border-radius:7px;font-size:15px;padding-left:11px}
  .read-more i{width:23px;height:23px;border:2px solid #ddd;border-radius:50%;display:inline-block}
  .hero-btn{left:213px;top:313px;width:152px;height:41px}
  .hint{font-size:9px;color:var(--muted);line-height:12px}
  .hero-hint{left:382px;top:322px}
  .hero-photo{left:797px;top:137px;width:206px;height:302px;background:radial-gradient(circle at 55% 35%,#f0d8c4,#dfe6ee 60%,#eef2f6);border-radius:4px}
  .slider-dots{left:900px;top:413px;display:flex;gap:5px;align-items:center}
  .slider-dots b{width:8px;height:8px;background:#333}
  .feature-arrow{top:515px;width:20px;height:20px;border-radius:50%;background:#e0e0e0;color:#777;font-size:12px;text-align:center;line-height:20px}
  .feature{top:485px;width:120px;text-align:center;font-size:11px;color:var(--muted);line-height:15px}
  .feature svg{display:block;margin:0 auto 10px}
  .monitor{left:210px;top:632px;width:366px;height:246px;background:#2e2e2e;border-radius:6px}
  .screen{left:16px;top:16px;width:334px;height:206px;background:linear-gradient(#c9d6e0,#9fb2c2)}
  .stand{left:350px;top:878px;width:90px;height:60px;background:linear-gradient(#e8e8e8,#cfcfcf);clip-path:polygon(15% 0,85% 0,100% 100%,0 100%)}
  .feature-copy{left:625px;top:642px;width:390px}
  .feature-copy h2{font-weight:400;font-size:19px;line-height:24px;margin-bottom:18px}
  .feature-copy h2 .r{color:var(--red)}.feature-copy h2 .b{color:var(--blue)}
  .feature-copy p{font-size:10.5px;line-height:15.5px;color:#555;margin-bottom:13px}
  .more-box{left:626px;top:874px;width:284px;height:67px;background:#ebebeb;border-radius:8px}
  .more-box .read-more{position:absolute;left:8px;top:14px;width:152px;height:41px}
  .more-box .hint{position:absolute;left:178px;top:22px}
  .footer{left:0;top:994px;width:1200px;height:187px;background:var(--footer)}
  .footer-nav{left:227px;top:1049px;display:flex;gap:30px;font-size:12.5px;color:var(--ink)}
  .footer-nav span:first-child{color:var(--red)}
  .footer-logo{left:827px;top:1040px;font-size:46px}
  .copyright{left:826px;top:1111px;font-size:9px;color:#555}
  .scrim{left:0;top:0;width:1200px;height:1181px;background:var(--scrim)}
  .modal{left:466px;top:173px;width:358px;height:413px;background:#fff;border-radius:14px}
  .close{left:322px;top:14px;width:24px;height:24px;background:#555;border-radius:4px;color:#fff;font-size:17px;font-weight:700;text-align:center;line-height:24px}
  .modal-logo{left:25px;top:40px;font-size:46px}
  .modal-tag{left:229px;top:72px;font-size:12.5px;color:#222}
  .field-label{left:63px;font-size:12px;color:#222}
  .field{left:58px;width:250px;height:33px;border:1px solid #aaa;border-radius:17px;box-shadow:inset 0 2px 3px rgba(0,0,0,.12)}
  .error{left:62px;top:271px;width:244px;height:26px;background:var(--red);color:#fff;font-size:10.5px;display:flex;align-items:center;gap:7px;padding-left:9px}
  .error::before{content:"";position:absolute;left:-5px;top:8px;border:5px solid transparent;border-left:0;border-right-color:var(--red)}
  .error i{width:12px;height:12px;border-radius:50%;background:#fff;color:var(--red);font-style:normal;font-size:9px;font-weight:700;text-align:center;line-height:12px}
  .register{left:67px;top:340px;font-size:9.5px;line-height:13px;text-decoration:underline;color:#333}
  .modal-btn{left:194px;top:334px;width:112px;height:41px;font-size:15px;font-weight:500}
</style>
</head>
<body>
  <div class="abs top-bar"></div>
  <div class="abs login-tab"><i></i>LOGIN</div>
  <div class="abs brand site-logo">Lumaport</div>
  <nav class="abs main-nav"><span>HOME</span><span>ABOUT IPV6</span><span>BENEFITS</span><span>TESTIMONIAL</span><span>CONTACT US</span></nav>

  <h1 class="abs hero-title" style="font-weight:400">IPv6 <span class="r">reduces the size</span> <span class="b">routing tables</span> and makes routing <span class="b">more</span> <span class="r">efficient</span> <span class="b">and</span> <span class="r">hierarchical</span>.</h1>
  <div class="abs read-more hero-btn"><i></i>Read More</div>
  <div class="abs hint hero-hint">Click here for<br>more details on IPv6</div>
  <div class="abs hero-photo" role="img" aria-label="Smiling support engineer with networked devices"></div>
  <div class="abs slider-dots"><span style="color:var(--blue)">◀</span><b></b><b></b><b></b><span style="color:var(--red)">▶</span></div>

  <div class="abs feature-arrow" style="left:209px">‹</div>
  <div class="abs feature" style="left:260px">
    <svg width="58" height="36"><rect x="23" y="0" width="12" height="9" fill="#3f7fb6"/><path d="M29 9v8M8 17h42M8 17v6M29 17v6M50 17v6" stroke="#555" stroke-width="2" fill="none"/><rect x="0" y="24" width="15" height="10" fill="#d8262c"/><rect x="22" y="24" width="15" height="10" fill="#d8262c"/><rect x="43" y="24" width="15" height="10" fill="#d8262c"/></svg>
    Efficient<br>Routing</div>
  <div class="abs feature" style="left:403px">
    <svg width="40" height="36"><path d="M20 0l14 14H26v10H14V14H6z" fill="#3f7fb6"/><rect x="4" y="28" width="32" height="7" fill="#d8262c"/></svg>
    Efficient<br>Packet Processing</div>
  <div class="abs feature" style="left:834px">
    <svg width="50" height="40"><circle cx="15" cy="8" r="7" fill="#d8262c"/><path d="M4 36c0-14 22-14 22 0z" fill="#3f7fb6"/><circle cx="27" cy="10" r="6" fill="#3f7fb6"/><path d="M26 28l7 7 14-16" stroke="#3f7fb6" stroke-width="4" fill="none"/></svg>
    Support For<br>New Services</div>
  <div class="abs feature-arrow" style="left:977px">›</div>

  <div class="abs monitor"><div class="abs screen" role="img" aria-label="Video still: world map with network connections and play button"></div></div>
  <div class="abs stand"></div>

  <section class="abs feature-copy">
    <h2><span class="r">IPv6</span> Also Implements <span class="b">Additional Features</span> Not Present in <span class="r">IPv4,</span> Feel The Differences</h2>
    <p>It simplifies aspects of address assignment , network renumbering and router announcements when changing network connectivity providers.</p>
    <p>The Internet operates by transferring data between hosts in packets that are routed across networks as specified by routing protocols.</p>
    <p>These packets require an addressing scheme, such as IPv4 or IPv6, to specify their source and destination addresses. Each host, computer or other device on the Internet requires an IP address in order to communicate.</p>
  </section>
  <div class="abs more-box"><div class="read-more"><i></i>Read More</div><div class="hint">Click here for<br>more details on IPv6</div></div>

  <footer class="abs footer"></footer>
  <nav class="abs footer-nav"><span>HOME</span><span>ABOUT IPV6</span><span>BENEFITS</span><span>TESTIMONIAL</span><span>CONTACT US</span></nav>
  <div class="abs brand footer-logo">Lumaport</div>
  <div class="abs copyright">Copyright ©2012 Lumaport, All Right Reserved</div>

  <div class="abs scrim"></div>
  <div class="abs modal" role="dialog" aria-label="Login area">
    <div class="abs close">×</div>
    <div class="abs brand modal-logo" style="font-size:40px">Lumaport</div>
    <div class="abs modal-tag">LOGIN AREA</div>
    <div class="abs field-label" style="top:170px">Username</div>
    <div class="abs field" style="top:197px"></div>
    <div class="abs field-label" style="top:240px">Password</div>
    <div class="abs field" style="top:266px"></div>
    <div class="abs error" style="top:317px"><i>!</i>Wrong Username / Password</div>
    <div class="abs register" style="top:380px">Not a member yet?<br>Click here to register</div>
    <div class="abs read-more modal-btn" style="top:370px"><i></i>Login</div>
  </div>
</body>
</html>
```